Tolvern Business Cards

Business card design. dont mind if new logo is suggested.
it would be for a security company.
our clients would be bigger security companies around Australia.
have a logo done but can be replaced. see attaached. like the colors.
Need company name, person name, designation, phone and email on front.
At back company logo and name. website saddress and 2 x license numbers
would like to have 2 different background color for both sidde

Industry/Entity Type

Security

Contact Information for Business Card

round corners, front should be light in color. need logo at back with webaddress and 2 x license numners

Font styles to use
Sans Serif

Colors
f37122
faa54b
f8ba93
0255a3
0592cd
85cae6
b3d448
9bcb3c
ffffff

Requirements
Must have
• see description
Nice to have
• see description
Should not have
• should not be difficult to read or hardd to find information on card.. lets say easy on eyes yet catchy

```html
<!DOCTYPE html>
<html lang="en">
<head>
<meta charset="utf-8">
<title>Tolvern Security Group – Business Cards</title>
<link href="https://fonts.googleapis.com/css2?family=EB+Garamond:wght@400;500;600&display=swap" rel="stylesheet">
<style>
  :root{
    --backdrop:#e9e4dc;
    --card:#ffffff;
    --navy:#1f2b63;
    --teal:#1ea7cc;
    --ink-soft:#7a7f8c;
    --rule:#b9bcc4;
    --dot-grey:#c9ccd6;
    --dot-teal:#bfe3ec;
  }
  *{box-sizing:border-box;margin:0;padding:0}
  html,body{width:1200px;height:802px;overflow:hidden}
  body{
    background:var(--backdrop);
    font-family:"EB Garamond",Georgia,serif;
    color:var(--navy);
    position:relative;
  }
  .card{
    position:absolute;
    width:540px;height:310px;
    background:var(--card);
    border-radius:22px;
    box-shadow:0 6px 18px rgba(60,50,30,.18);
    overflow:hidden;
  }
  .card--front{left:40px;top:246px}
  .card--back{left:620px;top:246px}

  .pattern-area{
    position:absolute;left:0;bottom:0;
    width:290px;height:190px;
    background:radial-gradient(ellipse at 30% 75%, var(--dot-teal) 0%, rgba(201,204,214,.55) 45%, rgba(255,255,255,0) 75%);
    opacity:.75;
  }

  .brand{
    position:absolute;right:30px;
    display:flex;align-items:center;gap:10px;
    font-size:21px;font-weight:600;letter-spacing:.04em;
    color:var(--navy);
    text-transform:uppercase;white-space:nowrap;
  }
  .brand__dot{width:16px;height:16px;border-radius:50%;background:var(--teal);flex:none}
  .card--front .brand{bottom:42px}
  .card--back .brand{bottom:100px;font-size:23px}

  .person{
    position:absolute;left:30px;top:52px;
    padding-right:18px;
    border-right:1px solid var(--rule);
    height:62px;
  }
  .person__name{font-size:22px;font-weight:600;letter-spacing:.05em;line-height:1.1}
  .person__role{font-size:12px;color:var(--ink-soft);margin-top:2px}

  .contact{
    position:absolute;left:188px;top:50px;
    font-size:12.5px;line-height:1.35;color:var(--ink-soft);
  }
  .contact__gap{height:8px}

  .web-info{
    position:absolute;left:30px;top:44px;
    font-size:14.5px;line-height:1.35;letter-spacing:.04em;color:var(--ink-soft);
  }
  .web-info__url{color:var(--navy);font-weight:500}
</style>
</head>
<body>

<section class="card card--front" aria-label="Front of business card">
  <div class="person">
    <p class="person__name">JOHN DOE</p>
    <p class="person__role">Director</p>
  </div>
  <div class="contact">
    <p>+63 900 555 0147</p>
    <p>john@tolvern.com</p>
    <div class="contact__gap"></div>
    <p>Dummy Street</p>
    <p>Dummy City, Dummy Country</p>
  </div>
  <div class="pattern-area" role="img" aria-label="Faint decorative dot pattern in grey and light teal"></div>
  <div class="brand"><span class="brand__dot"></span>Tolvern Security Group</div>
</section>

<section class="card card--back" aria-label="Back of business card">
  <div class="web-info">
    <p class="web-info__url">www.tolvern.com</p>
    <p>license no: XXXX XX | license no: XXXX XX</p>
  </div>
  <div class="pattern-area" role="img" aria-label="Faint decorative dot pattern in grey and light teal"></div>
  <div class="brand"><span class="brand__dot"></span>Tolvern Security Group</div>
</section>

</body>
</html>
```